Brindlepeak Tools Website Redesign Project

We need to design a site similar to the old one (https://www.brindlepeaktools.com/home) with an updated, fresh interface. There is a products page with linked PDF documents that need to be easily updated.

Coding

Coded - Design and coding required

Number of Pages Required

5+ page

```html
<!DOCTYPE html>
<html lang="en">
<head>
<meta charset="utf-8">
<title>Brindlepeak Tools – Downhole Tools Worldwide</title>
<link href="https://fonts.googleapis.com/css2?family=Urbanist:wght@400;500;600;700;800&display=swap" rel="stylesheet">
<style>
:root{
  --maroon:#8c1550;
  --maroon-dark:#6e0f3f;
  --teal:#0e94a8;
  --teal-dark:#0a7f91;
  --ink:#1d1d2b;
  --muted:#5b5b66;
  --line:#e3e3e8;
  --soft:#f5f5f6;
  --white:#ffffff;
}
*{box-sizing:border-box;margin:0;padding:0}
html,body{width:1200px;height:4461px;overflow:hidden;background:#fff}
body{font-family:"Urbanist",sans-serif;color:var(--ink);position:relative}
.abs{position:absolute}
.btn{position:absolute;display:inline-flex;align-items:center;justify-content:center;border-radius:20px;font-weight:700;font-size:12px;height:32px;padding:0 22px}
.btn-teal{background:var(--teal);color:#fff}
.btn-outline{border:2px solid var(--teal);color:var(--teal);background:#fff}
.btn-maroon{background:var(--maroon);color:#fff}
.eyebrow{font-size:11px;font-weight:700;color:var(--maroon);position:absolute;width:100%;text-align:center}
.heading{position:absolute;width:100%;text-align:center;font-size:30px;font-weight:400}
.heading b{font-weight:800}

/* header */
.topbar{position:absolute;left:823px;top:0;width:377px;height:22px;background:var(--maroon);color:#fff;font-size:11px;display:flex;align-items:center;justify-content:flex-end;gap:34px;padding-right:60px}
.topbar .phone{position:absolute;left:-823px}
.contactstrip{position:absolute;left:0;top:0;width:823px;height:22px;background:#fff}
.contactstrip span{position:absolute;right:40px;top:4px;font-size:11px;font-weight:600}
.header{position:absolute;top:22px;left:0;width:1200px;height:59px;background:#fff}
.brand{position:absolute;left:56px;top:8px}
.brand .name{font-size:20px;font-weight:800;color:var(--teal);display:flex;align-items:center;gap:7px}
.brand .dot{width:12px;height:12px;border-radius:50%;background:var(--maroon)}
.brand .tag{font-size:11px;color:var(--muted);margin-top:1px}
.nav{position:absolute;left:322px;top:22px;display:flex;gap:38px;font-size:12px;font-weight:700}
.nav .active{color:var(--teal);border-bottom:2px solid var(--teal)}
.nav-cta{left:1020px;top:12px;height:32px;font-size:11px}

/* hero */
.hero{position:absolute;top:81px;left:0;width:1200px;height:570px}
.hero-title{position:absolute;left:106px;top:110px;color:#fff;font-size:40px;font-weight:700;line-height:1.12}
.hero-sub{position:absolute;left:106px;top:210px;color:#fff;font-size:13px;line-height:1.4;width:470px}
.slider-dot{position:absolute;left:1064px;width:28px;height:28px;border-radius:50%;border:1.5px solid #fff;background:rgba(255,255,255,.2)}

/* about */
.about{position:absolute;top:648px;left:0;width:1200px;height:556px;background:var(--soft)}
.about-photo{position:absolute;left:200px;top:40px;width:354px;height:354px;border-radius:50%;border:4px solid #fff;background:radial-gradient(circle at 50% 35%,#c9d7e3,#5e88aa 55%,#1e4f7a)}
.badge{position:absolute;left:339px;top:314px;width:164px;height:164px;border-radius:50%;background:var(--maroon);border:5px solid #fff;color:#fff;text-align:center;padding-top:40px}
.badge b{font-size:38px;font-weight:500;display:block}
.badge span{font-size:11px;font-weight:600;line-height:1.2;display:block}
.about-text{position:absolute;left:612px;top:122px;width:420px}
.about-text h2{font-size:30px;font-weight:400;line-height:1.25;margin:22px 0 26px}
.about-text h2 b{font-weight:800}
.about-text p{font-size:11px;line-height:1.75;color:var(--muted)}

/* products */
.products{position:absolute;top:1204px;left:0;width:1200px;height:500px}
.product{position:absolute;top:161px;width:250px}
.product .pic{height:150px}
.product .label{display:flex;justify-content:space-between;font-size:13px;font-weight:700;padding:22px 12px 12px;border-bottom:2px solid var(--maroon)}

/* why */
.why-band{position:absolute;top:1705px;left:0;width:1200px;height:331px;background:linear-gradient(100deg,var(--maroon-dark),var(--maroon))}
.why-panel{position:absolute;top:1868px;left:106px;width:990px;height:361px;background:#fff;box-shadow:0 8px 30px rgba(0,0,0,.08)}
.why-photo{position:absolute;left:0;top:0;width:244px;height:361px;background:linear-gradient(160deg,#9fb7cc,#3a6791 60%,#1c3a5c)}
.why-list{position:absolute;left:286px;top:64px;width:168px}
.why-list li{list-style:none;font-size:13px;font-weight:600;padding:12px 0 12px 0;border-bottom:1px solid var(--line)}
.why-list li.on{color:var(--maroon)}
.why-detail{position:absolute;left:495px;top:0;width:495px;height:361px;background:#efefef;border-left:3px solid var(--maroon);padding:62px 74px}
.why-detail h3{font-size:22px;font-weight:600;margin:18px 0 10px}
.why-detail p{font-size:11px;line-height:1.7;color:#444}

/* testimonials */
.tcard{position:absolute;top:2396px;width:364px;height:181px;background:#fff;box-shadow:0 6px 22px rgba(0,0,0,.08)}
.tcard .avatar{position:absolute;left:-28px;top:0;width:62px;height:62px;background:linear-gradient(#c9a993,#8a6a58)}
.tcard .body{position:absolute;left:62px;top:22px;width:270px;font-size:10px;line-height:1.55;color:#444}
.stars{color:var(--maroon);font-size:13px;letter-spacing:2px;margin-bottom:6px}
.tcard .who{margin-top:14px;color:var(--maroon);font-weight:700;font-size:11px}
.circle-nav{position:absolute;top:2611px;width:30px;height:30px;border-radius:50%;border:1.5px solid var(--maroon);color:var(--maroon);display:flex;align-items:center;justify-content:center;font-size:14px}

/* career */
.career{position:absolute;top:2714px;left:0;width:1200px;height:351px;overflow:hidden}
.career-text{position:absolute;left:106px;top:80px;color:#fff}
.career-text h2{font-size:30px;font-weight:400;margin:10px 0 18px}
.career-text h2 b{font-weight:800}
.career-text p{font-size:19px;line-height:1.5}

/* news */
.news{position:absolute;top:3224px;width:313px}
.news .pic{height:156px}
.news .cap{margin:-18px 24px 0;background:#fff;position:relative;text-align:center;padding:22px 10px 22px;box-shadow:0 4px 16px rgba(0,0,0,.06)}
.news .date{font-size:10px;color:var(--teal);font-weight:700}
.news .title{font-size:13px;font-weight:600;margin-top:6px;line-height:1.35}

/* contact */
.contact-form{position:absolute;left:342px;top:3840px;width:512px}
.field{position:absolute;height:34px;background:#fff;font-size:11px;padding:8px 10px;color:#444}

/* footer */
.footer-col h4{font-size:12px;font-weight:700;color:var(--teal);margin-bottom:14px}
.footer-col p,.footer-col li{font-size:11px;color:#555;line-height:1.9;list-style:none}
.social{position:absolute;left:985px;width:30px;height:30px;border-radius:50%;border:1.5px solid var(--maroon);display:flex;align-items:center;justify-content:center}
.social i{width:8px;height:8px;background:var(--maroon);border-radius:2px;display:block}
</style>
</head>
<body>

<!-- Top bar & header -->
<div class="contactstrip"><span>&#9742; (555) 014-2270</span></div>
<div class="topbar"><span>&#9993; sales@brindlepeaktools.com</span></div>
<header class="header">
  <div class="brand">
    <div class="name"><span class="dot"></span>Brindlepeak Tools</div>
    <div class="tag">Downhole Tools Worldwide</div>
  </div>
  <nav class="nav">
    <span class="active">Home</span><span>Why Brindlepeak</span><span>Products</span><span>Worldwide Reps</span><span>Review</span><span>News</span><span>News</span><span>Careers</span>
  </nav>
  <span class="btn btn-outline nav-cta">Free Consultation</span>
</header>

<!-- Hero -->
<section class="hero">
  <svg width="1200" height="570" class="abs" style="left:0;top:0">
    <defs>
      <linearGradient id="sky" x1="0" y1="0" x2="0" y2="1">
        <stop offset="0" stop-color="#3c3a40"/><stop offset=".45" stop-color="#b07a48"/><stop offset="1" stop-color="#5a4432"/>
      </linearGradient>
    </defs>
    <polygon points="0,0 1200,0 1200,366 600,534 0,366" fill="url(#sky)" role="img" aria-label="Photo of an oilfield pump jack at sunset"/>
    <polyline points="0,420 600,567 1200,420" fill="none" stroke="var(--teal)" stroke-width="5" clip-path="none"/>
    <polygon points="0,366 600,534 1200,366 1200,570 0,570" fill="#fff"/>
    <polygon points="440,508 600,565 760,508 600,548" fill="var(--teal)"/>
  </svg>
  <h1 class="hero-title">Industry Leading<br>Downhole Tools Worldwide</h1>
  <p class="hero-sub">Brindlepeak Tools Inc. is a Canadian based manufacturer and supplier of today's most innovative and reliable downhole tools.</p>
  <span class="btn btn-teal" style="left:106px;top:265px">Free Consultation</span>
  <span class="slider-dot" style="top:145px"></span>
  <span class="slider-dot" style="top:182px"></span>
</section>

<!-- About -->
<section class="about">
  <div class="about-photo" role="img" aria-label="Photo of an offshore oil platform at sea"></div>
  <div class="badge"><b>40</b><span>YEARS OF<br>EXPERIENCE</span></div>
  <div class="about-text">
    <div style="font-size:11px;font-weight:700;color:var(--maroon)">About us</div>
    <h2>Brindlepeak Tools Inc. is a <b>Canadian Based Manufacturer and Supplier</b></h2>
    <p>Our goal is to become a global leader in supplying completion and liner hanger systems to the oil and gas industry. We continue to gather larger market shares both domestically, and internationally as our high-quality products continue to prove themselves to our customers in the field...</p>
  </div>
  <span class="btn btn-outline" style="left:612px;top:394px">Discover More</span>
</section>

<!-- Products -->
<section class="products">
  <div class="eyebrow" style="top:80px">Products</div>
  <h2 class="heading" style="top:108px">Canadian Made <b>Downhole Oilfield Tools</b></h2>
  <div class="product" style="left:200px"><div class="pic" role="img" aria-label="Photo of a pump jack under a pink dusk sky" style="background:linear-gradient(#6a6f8f,#c98a8a 55%,#5a3e36)"></div><div class="label"><span>Completion &amp; Service Tools</span><span>&#8599;</span></div></div>
  <div class="product" style="left:475px"><div class="pic" role="img" aria-label="Photo of a drilling rig under blue sky" style="background:linear-gradient(#8fb2d8,#c8d8e8 60%,#7e8a70)"></div><div class="label"><span>Liner Systems</span><span>&#8599;</span></div></div>
  <div class="product" style="left:750px"><div class="pic" role="img" aria-label="Photo of an offshore platform" style="background:linear-gradient(#6aa3d6,#b8d4ec 55%,#2d6a96)"></div><div class="label"><span>Inflatables</span><span>&#8599;</span></div></div>
  <span class="btn btn-outline" style="left:535px;top:398px;height:30px;font-size:11px">Free Consultation</span>
</section>

<!-- Why -->
<section class="why-band" role="img" aria-label="Faint photo of refinery towers behind a maroon overlay">
  <div class="eyebrow" style="top:78px;color:#f2d9e5">Why Choose Brindlepeak Tools</div>
  <h2 class="heading" style="top:105px;color:#fff">Uncompromised <b>Service and Expertise</b></h2>
</section>
<div class="why-panel">
  <div class="why-photo" role="img" aria-label="Photo of an engineer inspecting a machined part"></div>
  <ul class="why-list">
    <li>Brindlepeak Liners</li><li>Brindlepeak Inflates</li><li class="on">Engineering</li><li>Quality Policy</li><li style="border:0">Health and Safety</li>
  </ul>
  <div class="why-detail">
    <svg width="56" height="56" viewBox="0 0 56 56"><circle cx="28" cy="30" r="22" fill="none" stroke="var(--maroon)" stroke-width="2.5"/><path d="M14 26a14 14 0 0 1 28 0z" fill="var(--maroon)"/><rect x="12" y="26" width="32" height="4" fill="var(--maroon)"/><circle cx="28" cy="40" r="6" fill="none" stroke="var(--maroon)" stroke-width="2.5"/></svg>
    <h3>Engineering</h3>
    <p>Brindlepeak's engineering and design team design team has more than 35 years of completion engineering design experience. The engineering team is located in-house at our manufacturing facility in Calgary, Canada...</p>
    <span class="btn btn-teal" style="position:relative;margin-top:22px;height:30px;font-size:11px">Explore More</span>
  </div>
</div>

<!-- Testimonials -->
<div class="eyebrow" style="top:2311px">Testimonials</div>
<h2 class="heading" style="top:2337px">Happy <b>Clients Say</b></h2>
<div class="tcard" style="left:416px;margin-left:-192px">
  <div class="avatar" role="img" aria-label="Portrait of a client" style="left:0"></div>
  <div class="body" style="left:88px"><div class="stars">★★★★★</div>" There are many variations of passages of lorem ipsum available, but the majority have suffered alteration in some form, by injected humour, or randomised words which don't look even..."<div class="who">Standard Chunk</div><div style="color:#666">Lorem ipsum</div></div>
</div>
<div class="tcard" style="left:612px">
  <div class="avatar" role="img" aria-label="Portrait of a client" style="left:0;background:linear-gradient(#bfbfbf,#6d6d6d)"></div>
  <div class="body" style="left:88px"><div class="stars">★★★★★</div>" There are many variations of passages of lorem ipsum available, but the majority have suffered alteration in some form, by injected humour, or randomised words which don't look even..."<div class="who">Standard Chunk</div><div style="color:#666">Lorem ipsum</div></div>
</div>
<div class="abs" style="left:362px;top:2626px;width:476px;height:1px;background:var(--line)"></div>
<span class="circle-nav" style="left:546px">&#8249;</span>
<span class="btn btn-outline" style="left:711px;top:2611px;height:30px;font-size:11px;background:#fff">View All</span>
<span class="circle-nav" style="left:958px">&#8250;</span>

<!-- Career -->
<section class="career">
  <div class="abs" role="img" aria-label="Photo of a worker with a tablet beside a pump jack" style="left:0;top:0;width:1200px;height:351px;background:linear-gradient(90deg,#c69a5c,#e8c78a 40%,#7a8aa0)"></div>
  <svg width="1200" height="351" class="abs" style="left:0;top:0"><polygon points="0,0 763,0 563,351 0,351" fill="var(--teal)"/></svg>
  <div class="career-text">
    <div style="font-size:11px;font-weight:700">Career</div>
    <h2>Get a <b>Rewarding Career</b></h2>
    <p>Are you results orientated, and a true team player,<br>if so, apply and send us your resume.</p>
  </div>
  <span class="btn btn-maroon" style="left:106px;top:255px;height:30px;font-size:11px">Apply Now!</span>
</section>

<!-- News -->
<div class="eyebrow" style="top:3146px">Latest News</div>
<h2 class="heading" style="top:3170px">Recent <b>Articles</b></h2>
<div class="news" style="left:443px;margin-left:-168px">
  <div class="pic" role="img" aria-label="Photo of yellow pipework on an offshore rig" style="background:linear-gradient(#4f88c2,#d8b23a 60%,#3f5e7a)"></div>
  <div class="cap"><div class="date">12 December '18</div><div class="title">NEW TOOL: Ti6 Sucessful Test<br>(Insert PCP Packer)</div></div>
</div>
<div class="news" style="left:612px">
  <div class="pic" role="img" aria-label="Photo of refinery towers" style="background:linear-gradient(#5f9ad0,#8db07a 55%,#c9ccc8)"></div>
  <div class="cap"><div class="date">11 January '14</div><div class="title">Successful Test - 4 ½" Inflatable<br>Casing Packer (ECP) SFT Elastomer</div></div>
</div>
<span class="btn btn-outline" style="left:711px;top:3521px;height:30px;font-size:11px">View All</span>

<!-- Contact -->
<svg width="1200" height="500" class="abs" style="left:0;top:3614px">
  <polygon points="0,173 600,6 1200,173 1200,500 0,500" fill="var(--maroon)" role="img" aria-label="Faint refinery silhouette behind a maroon overlay"/>
  <polyline points="370,70 600,3 830,70" fill="none" stroke="var(--teal)" stroke-width="5"/>
</svg>
<div class="eyebrow" style="top:3752px;color:#fff">Need a Part?</div>
<h2 class="heading" style="top:3778px;color:#fff">Have a <b>Question?</b></h2>
<div class="contact-form">
  <div class="field" style="left:0;top:0;width:250px">Name</div>
  <div class="field" style="left:262px;top:0;width:250px">Phone</div>
  <div class="field" style="left:0;top:50px;width:250px">Email</div>
  <div class="field" style="left:262px;top:50px;width:250px">Company</div>
  <div class="field" style="left:0;top:100px;width:512px;height:62px">Message...</div>
</div>
<span class="btn btn-teal" style="left:711px;top:4018px;height:30px;font-size:11px">Submit</span>

<!-- Footer -->
<footer>
  <div class="brand" style="top:4208px;left:200px">
    <div class="name"><span class="dot"></span>Brindlepeak Tools</div>
    <div class="tag">Downhole Tools Worldwide</div>
  </div>
  <div class="footer-col abs" style="left:628px;top:4196px;width:240px">
    <h4>Contact Us</h4>
    <p>&#9742; (555) 018-4410</p>
    <p>&#9993; sales@brindlepeaktools.com</p>
    <p>&#9679; Unit 7, 1180 Ridgeline Rd SE, Calgary, Alberta,<br>&nbsp;&nbsp;&nbsp;Canada, T2X 0A1</p>
    <p style="color:var(--teal);font-weight:700;margin-top:6px">Get Directions &#8599;</p>
  </div>
  <div class="footer-col abs" style="left:896px;top:4196px;width:240px">
    <h4>Company</h4>
    <ul style="float:left;width:112px"><li>Home</li><li>Why Brindlepeak</li><li>Products</li><li>Worldwide Reps</li><li>Testimonials</li><li>News</li></ul>
    <ul style="float:left"><li>Careers</li><li>Contact</li><li>Privacy Policy</li></ul>
  </div>
  <span class="social" style="left:1135px;top:4196px"><i></i></span>
  <span class="social" style="left:1135px;top:4234px"><i></i></span>
  <div class="abs" style="left:362px;top:4390px;width:476px;height:1px;background:var(--line)"></div>
  <div class="abs" style="left:0;top:4414px;width:1200px;text-align:center;font-size:11px;color:#555">© 2024 <b style="color:var(--maroon)">Brindlepeak Tools Inc.</b> All Rights Reserved</div>
</footer>

</body>
</html>
```